high performance web based fitness

High end online fitness portal. State of the art online fitness and high performance training. Also catering to all who are interested in a personally designed online training program by Olympic Gold Medalist "Dario Fenwell" (dariofenwell-example.com)
Based in the Toronto area.
Online fitness consulting.
Including picture and video instruction of exercises. Downloadable fitness programs.
eCommerce ready.

(or just have skills to convert from site, i.e. wordpress, weebly)

Industry/Entity Type

Catering

```html
<!DOCTYPE html>
<html lang="en">
<head>
<meta charset="utf-8">
<title>Kinetra — High Performance Personal Training</title>
<link href="https://fonts.googleapis.com/css2?family=Ubuntu:wght@300;400;500;700&display=swap" rel="stylesheet">
<style>
:root{
  --green:#8cc617;
  --green-dark:#5f9a08;
  --green-light:#a9dc2c;
  --top:#2d2d2d;
  --hero:#2a2a2a;
  --deep:#151515;
  --panel:#222;
  --base:#262626;
  --text:#e8e8e8;
  --faint:#8a8a8a;
}
*{box-sizing:border-box;margin:0;padding:0}
html,body{width:832px;height:1200px;overflow:hidden;background:var(--deep)}
body{font-family:'Ubuntu',sans-serif;color:var(--text);position:relative}
.abs{position:absolute}

.topbar{left:0;top:0;width:832px;height:82px;background:var(--top);border-top:5px solid #1d1d1d}
.brand{left:50px;top:22px;font-size:35px;font-weight:400;color:#fff;letter-spacing:.5px}
.search{left:622px;top:43px;width:168px;height:22px;background:#3c3c3c;border:1px solid #474747;border-radius:2px;font-size:8px;font-style:italic;color:#aaa;padding:6px 10px}
.search svg{position:absolute;right:8px;top:6px}

.nav{left:0;top:82px;width:832px;height:42px;background:linear-gradient(#9fd724,#7fbb0d 60%,#6fa80a);display:flex;border-bottom:1px solid #4e7a06}
.nav a{display:flex;align-items:center;justify-content:center;color:#fff;font-weight:500;font-size:11px;text-decoration:none;letter-spacing:.1px;border-right:1px solid #6a9f0a;box-shadow:1px 0 0 #a8dc3a}
.nav a:last-child{border-right:0;box-shadow:none}

.hero{left:0;top:124px;width:832px;height:330px;background:var(--hero)}
.hero-title{left:43px;top:56px;font-size:34px;color:var(--green);font-weight:300}
.hero-sub{left:43px;top:96px;font-size:25px;color:#fff;font-weight:300}
.hero-text{left:45px;top:132px;width:330px;font-size:9.6px;line-height:15px;color:#cfcfcf;font-weight:300}
.btn-main{left:43px;top:189px;width:139px;height:33px;border-radius:3px;background:linear-gradient(var(--green-light),var(--green-dark));color:#fff;font-size:11.5px;font-weight:500;display:flex;align-items:center;justify-content:center}
.dots{left:49px;top:268px;display:flex;gap:3px}
.dots i{width:9px;height:9px;border-radius:50%;background:#666}
.dots i:first-child{background:var(--green)}
.hero-frame{left:413px;top:29px;width:381px;height:257px;background:#eee;padding:5px;box-shadow:0 6px 12px rgba(0,0,0,.5)}
.hero-photo{width:100%;height:100%;background:linear-gradient(160deg,#b9c2c8,#6f8fb9 45%,#c89a6c)}

.services{left:0;top:454px;width:832px;height:216px;background:repeating-linear-gradient(45deg,#313131 0 2px,#353535 2px 4px)}
.svc{top:0;width:177px}
.svc h3{position:absolute;top:22px;left:0;font-size:18px;font-weight:300;color:#fff;white-space:nowrap}
.svc p{position:absolute;top:47px;left:2px;font-size:9px;color:#ddd;white-space:nowrap}
.svc .pic{position:absolute;top:64px;left:0;width:177px;height:84px;border:2px solid #ddd}
.svc .more{position:absolute;top:158px;left:2px;width:91px;height:25px;border:1px solid #4a4a4a;background:#2a2a2a;border-radius:2px;font-size:9px;color:#ccc;display:flex;align-items:center;justify-content:center}

.media{left:0;top:670px;width:832px;height:314px;background:linear-gradient(#161616,#111)}
.sec-title{font-size:17.5px;font-weight:300;color:#fff}
.thumb{width:73px;height:60px;border:2px solid #eee}
.video{left:301px;top:743px;width:257px;height:192px;border:1px solid #555;background:linear-gradient(150deg,#c8d2d8,#e8b98b 50%,#c46f36)}
.play{left:410px;top:821px}
.controls{left:302px;top:912px;width:255px;height:22px;background:rgba(20,20,20,.9);display:flex;align-items:center;padding:0 7px;gap:7px;font-size:7px;color:#ddd}
.track{flex:1;height:2px;background:#666;position:relative}
.track b{position:absolute;left:0;top:-4px;width:2px;height:10px;background:#eee}

.dl{left:576px;top:705px;width:222px;height:230px;background:var(--panel);border:1px solid #2c2c2c;border-radius:3px}
.dl-head{height:64px;background:#2c2c2c;padding:14px 22px;font-size:16.5px;font-weight:500;color:var(--green);line-height:21px}
.dl h4{position:absolute;left:22px;top:79px;font-size:10px;font-weight:400;color:#eee}
.dl p{position:absolute;left:22px;top:97px;width:185px;font-size:8px;line-height:15.3px;color:var(--faint)}
.btn-dl{left:25px;top:168px;width:106px;height:26px;border-radius:2px;background:linear-gradient(var(--green-light),var(--green-dark));font-size:9px;font-weight:500;color:#fff;display:flex;align-items:center;justify-content:center}

.footer{left:0;top:984px;width:832px;height:178px;background:linear-gradient(#404040,#333)}
.fcol{top:31px}
.fcol h5{font-size:12px;font-weight:400;color:#fff;margin-bottom:8px}
.fcol li{list-style:none;font-size:9.4px;color:#ccc;line-height:17.5px;font-weight:300}
.fdiv{top:36px;width:1px;height:96px;background:#555}
.social{display:flex;gap:2px;margin-top:6px}
.social i{width:22px;height:22px;border-radius:50%;background:var(--green)}

.base{left:0;top:1162px;width:832px;height:38px;background:var(--base);font-size:8.6px;color:#aaa;font-weight:300}
.base .copy{left:31px;top:13px}
.base .legal{right:25px;top:13px}
</style>
</head>
<body>

<header class="topbar abs">
  <div class="brand abs">Kinetra</div>
  <div class="search abs">Search here..
    <svg width="6" height="8" viewBox="0 0 6 8"><path d="M1 0l5 4-5 4z" fill="#999"/></svg>
  </div>
</header>

<nav class="nav abs">
  <a style="width:96px;padding-left:30px">HOME</a>
  <a style="width:84px">ABOUT US</a>
  <a style="width:80px">SERVICES</a>
  <a style="width:107px">TESTIMONIALS</a>
  <a style="width:159px">BOOK AN APPOINTMENT</a>
  <a style="width:78px">GALLERY</a>
  <a style="width:59px">BLOG</a>
  <a style="width:52px">FAQ</a>
  <a style="width:84px">CONTACT</a>
</nav>

<section class="hero abs">
  <h1 class="hero-title abs">New High Performance</h1>
  <h2 class="hero-sub abs">Personal Training Portal</h2>
  <p class="hero-text abs">Curabitur vel mi sit amet magna malesuada ultrices. Ut nisi erat, fermentum vel, congue id, euismod in, elit. Fusce ultricies, orci ac feugiat suscipit, leo massa sodales velit, et scelerisque mi tortor at ipsum.</p>
  <div class="btn-main abs">Get Register Now</div>
  <div class="dots abs"><i></i><i></i><i></i><i></i></div>
  <div class="hero-frame abs"><div class="hero-photo" role="img" aria-label="Senior man doing push-ups on a blue mat in a gym"></div></div>
</section>

<section class="services abs">
  <div class="svc abs" style="left:32px">
    <h3>Training</h3><p>Certified high performance specialists...</p>
    <div class="pic" role="img" aria-label="Trainer assisting a client with a resistance band stretch" style="background:linear-gradient(120deg,#e9e9e9,#9aa1ad 55%,#3b3f4a)"></div>
    <div class="more">FIND OUT MORE</div>
  </div>
  <div class="svc abs" style="left:231px">
    <h3>Functional Therapy</h3><p>Certified functional specialists</p>
    <div class="pic" role="img" aria-label="Therapist treating a woman lying on a massage table" style="background:linear-gradient(120deg,#c9cfc0,#e8e4dc 50%,#b59a84)"></div>
    <div class="more">FIND OUT MORE</div>
  </div>
  <div class="svc abs" style="left:430px">
    <h3>Nutrition</h3><p>breaking nutritional information...</p>
    <div class="pic" role="img" aria-label="Assorted fresh vegetables" style="background:linear-gradient(120deg,#c2261c,#e56c1d 40%,#5f8e2a 70%,#d9c35a)"></div>
    <div class="more">FIND OUT MORE</div>
  </div>
  <div class="svc abs" style="left:628px">
    <h3>Consulting</h3><p>I person / phone / video call.</p>
    <div class="pic" role="img" aria-label="Doctor consulting with a senior patient" style="background:linear-gradient(120deg,#e5e8ec,#b8c4d6 50%,#7d97bf)"></div>
    <div class="more">FIND OUT MORE</div>
  </div>
</section>

<section class="media abs">
  <h3 class="sec-title abs" style="left:34px;top:44px">Photo Gallery</h3>
  <div class="thumb abs" style="left:34px;top:74px;background:linear-gradient(135deg,#f2f2f2,#c83a2a 50%,#7fae36)" role="img" aria-label="Fruit and measuring tape"></div>
  <div class="thumb abs" style="left:118px;top:74px;background:linear-gradient(135deg,#d6e6f2,#c89a7c)" role="img" aria-label="Woman drinking a glass of milk"></div>
  <div class="thumb abs" style="left:201px;top:74px;background:linear-gradient(135deg,#dfe3e8,#3a4a6a)" role="img" aria-label="Woman lifting a dumbbell"></div>
  <div class="thumb abs" style="left:34px;top:140px;background:linear-gradient(135deg,#bcd0de,#2d72b8)" role="img" aria-label="Smiling senior man in blue shirt"></div>
  <div class="thumb abs" style="left:118px;top:140px;background:linear-gradient(135deg,#f4f4f4,#b7a296)" role="img" aria-label="Senior man with towel after workout"></div>
  <div class="thumb abs" style="left:201px;top:140px;background:linear-gradient(135deg,#8a9aa8,#e08a2c)" role="img" aria-label="Woman exercising on a rowing machine"></div>
  <div class="thumb abs" style="left:34px;top:206px;background:linear-gradient(135deg,#f0f0f0,#86c03a 60%,#d9a08a)" role="img" aria-label="Woman biting a green apple"></div>
  <div class="thumb abs" style="left:118px;top:206px;background:linear-gradient(135deg,#e4e7ea,#9aa0a8)" role="img" aria-label="Woman holding a water bottle in a gym"></div>
  <div class="thumb abs" style="left:201px;top:206px;background:linear-gradient(135deg,#f2f2f2,#7aa74a 50%,#d8d2c4)" role="img" aria-label="Fresh green salad"></div>

  <h3 class="sec-title abs" style="left:301px;top:46px">Watch Our Video</h3>
</section>

<div class="video abs" role="img" aria-label="Two women stretching in a fitness class"></div>
<svg class="play abs" width="38" height="38" viewBox="0 0 38 38"><circle cx="19" cy="19" r="17" fill="#111" stroke="#fff" stroke-width="2.5"/><path d="M15 12l11 7-11 7z" fill="#fff"/></svg>
<div class="controls abs">
  <svg width="14" height="14" viewBox="0 0 14 14"><circle cx="7" cy="7" r="6" fill="none" stroke="#eee" stroke-width="1.2"/><path d="M5.5 4.5l4 2.5-4 2.5z" fill="#eee"/></svg>
  <div class="track"><b></b></div>
  <span>1:05</span>
  <svg width="12" height="10" viewBox="0 0 12 10"><path d="M0 3h3l3-3v10l-3-3H0z" fill="#ddd"/><path d="M8 2.5q2 2.5 0 5M9.5 1q3.5 4 0 8" fill="none" stroke="#ddd" stroke-width="1"/></svg>
</div>

<aside class="dl abs">
  <div class="dl-head">Downloading<br>Fitness Program</div>
  <h4>Nunc tempus felis vitae urna.</h4>
  <p>Vivamus porttitor, neque at volutpat rutrum, purus nisi eleifend libero, a tempus libero lectus feugiat felis. Morbi diam mauris, viverra in, gravida eu, mattis in, ante.</p>
  <div class="btn-dl abs">DOWNLOAD NOW</div>
</aside>

<footer class="footer abs">
  <div class="fcol abs" style="left:44px"><h5>Information</h5><ul><li>Home</li><li>About Us</li><li>What We Do</li><li>Why Choose Us</li></ul></div>
  <div class="fdiv abs" style="left:148px"></div>
  <div class="fcol abs" style="left:186px"><h5>Why We Are</h5><ul><li>Fitness</li><li>Nutritions</li><li>Body Treatment</li><li>Health</li></ul></div>
  <div class="fdiv abs" style="left:285px"></div>
  <div class="fcol abs" style="left:327px"><h5>Support</h5><ul><li>Recent Blog</li><li>FAQ</li><li>Customer Support</li><li>Recent Blog</li></ul></div>
  <div class="fdiv abs" style="left:435px"></div>
  <div class="fcol abs" style="left:469px"><h5>Contact Us</h5><ul><li>Download Program</li><li>Term of Use</li><li>Contact Info</li><li>Get Connected</li></ul></div>
  <div class="fdiv abs" style="left:582px"></div>
  <div class="fcol abs" style="left:613px;top:32px"><h5>Get In Touch</h5><div class="social"><i></i><i></i><i></i><i></i></div></div>
</footer>

<div class="base abs">
  <span class="copy abs">Copyright © 2013 Company name. All Rights Reserved.</span>
  <span class="legal abs">Privacy Policy &nbsp;|&nbsp; Terms of Services</span>
</div>

</body>
</html>
```